Website/Logo Design

We need a logo and website design for an opinion mining startup called VantaLume. Our technology mines the web to automatically discover what people are saying about brands, products, etc. The project we are fielding here is for our informational, public-facing website. In its initial incarnation, it will simply be a vehicle for marketing materials and information on our company and its offerings, but it should be flexible enough to expand as more content/functionality is added.

Some designs we like are:
http://www.tradewhisk.example
http://www.gorvantel.example
http://www.kfz.example
http://www.lintwharf.example
http://moxbarrel.example
http://trundlemq.example
http://www.zopla.example
Updates

All, please try to shy away from using a photo of a person as the focal point of the design.  Our company is more technological than social.

Target Market(s)

Primarily businesses interested in sentiment analysis (typically companies involved in advertising, market research, PR, etc.)

Industry/Entity Type

It Company

Requirements
Must have
• We are looking for a clean, modern, and professional design. This includes a logo, homepage, and internal page if it will differ from the homepage.
Nice to have
• It would be excellent if you could provide an HTML mockup if your design is chosen.
Should not have
• Flash, excessive bells and whistles

```html
<!DOCTYPE html>
<html lang="en">
<head>
<meta charset="utf-8">
<title>VantaLume</title>
<link rel="stylesheet" href="https://fonts.googleapis.com/css2?family=Open+Sans:wght@400;600&display=swap">
<style>
:root{
  --bg:#e6e6e8;
  --ink:#6a6a6e;
  --ink-dark:#4a4a4e;
  --heading:#3c3c40;
  --purple:#5b3f8a;
  --purple-dark:#3f2a66;
  --purple-link:#6a3fa6;
  --pink:#d58ac6;
  --pill:#a9a9ad;
  --pill-text:#ffffff;
  --band-grey:#9c9c9f;
  --white:#ffffff;
}
*{margin:0;padding:0;box-sizing:border-box}
html,body{width:1200px;height:1128px;overflow:hidden}
body{
  font-family:"Open Sans",Arial,sans-serif;
  color:var(--ink);
  background:
    radial-gradient(ellipse 520px 260px at 330px 120px,#ffffff 0%,rgba(255,255,255,0) 100%),
    linear-gradient(#cfcfd2 0,var(--bg) 260px,var(--bg) 100%);
  position:relative;
}
.abs{position:absolute}
.brand{left:87px;top:88px;display:flex;align-items:center;gap:12px}
.brand-name{font-size:50px;font-weight:400;color:#5c5577;letter-spacing:-1px}
.brand-mark{width:66px;height:66px;background:var(--purple);border-radius:8px}
.nav{top:120px;left:0;width:1200px;height:28px}
.nav a{position:absolute;top:0;height:27px;line-height:27px;text-align:center;border-radius:14px;
  background:var(--pill);color:var(--pill-text);font-size:15px;text-decoration:none;
  box-shadow:0 3px 6px rgba(0,0,0,.15)}
.nav a.active{background:var(--purple-dark)}
.hero{left:39px;top:190px;width:1130px;height:257px;border-radius:10px 10px 0 0;
  background:linear-gradient(120deg,#eef0fb 0%,#ffffff 40%,#ffffff 100%)}
.hero-q{right:438px;text-align:right;font-size:18.5px;color:#8a8d99;width:700px}
.hero-q em{font-style:normal;color:var(--pink)}
.cta{left:478px;top:370px;width:306px;height:46px;border-radius:4px;
  background:linear-gradient(#b49ad8,#8d6cbd);color:#fff;font-size:18.5px;
  line-height:46px;text-align:center}
.cta-tail{left:720px;top:414px}
.hero-art{left:822px;top:250px;width:330px;height:155px;border-radius:6px;
  background:radial-gradient(ellipse at 45% 45%,#9b7ac9 0%,#c9c9d3 45%,rgba(240,240,245,0) 80%)}
.band{left:39px;top:447px;width:1130px;height:120px;border-radius:0 0 8px 8px;
  background:linear-gradient(#4d3479,#5e4490)}
.band-item{top:26px;color:#fff;font-size:15px;line-height:20.5px;width:260px}
.band-icon{top:32px;width:52px;height:52px;border-radius:8px}
.divider{top:20px;width:1px;height:80px;background:rgba(255,255,255,.2)}
h2{font-size:24px;font-weight:400;color:var(--heading)}
.body{font-size:16px;line-height:23px;color:#808084}
.btn-small{left:257px;top:780px;width:150px;height:27px;border-radius:14px;background:#c6c6c9;
  color:#fff;font-size:15px;line-height:27px;text-align:center}
.services{left:452px;top:663px;width:340px;list-style:none}
.services li{position:relative;padding-left:30px;color:var(--purple-link);font-size:16px;line-height:20px}
.services svg{position:absolute;left:0;top:3px}
.contact{left:825px;top:663px;font-size:16px;line-height:23.5px;color:#808084}
.contact strong{font-weight:600;color:var(--ink-dark)}
.contact a{color:var(--purple-link);text-decoration:none}
.clients{left:39px;top:926px;width:1130px;height:101px;border-radius:8px;
  background:linear-gradient(90deg,#a4a4a7,#8e8e91)}
.clients-label{left:48px;top:38px;color:#fff;font-size:18px}
.client{top:38px;width:140px;text-align:center;font-size:20px;font-weight:600;color:#d9d9dc}
.client.hover{color:#fff}
.footer{top:1055px;font-size:13px;color:#77777b}
.footer a{color:var(--purple-link);text-decoration:none}
.social{top:1052px;display:flex;align-items:center;gap:4px;font-size:11px;color:#77777b}
.social span.sq{width:14px;height:14px;background:#8a8a8e;border-radius:2px;display:inline-block}
</style>
</head>
<body>

<div class="abs brand"><span class="brand-name">VantaLume</span><span class="brand-mark"></span></div>

<nav class="abs nav">
  <a style="left:517px;width:150px">About VantaLume</a>
  <a style="left:689px;width:130px">How We Work</a>
  <a class="active" style="left:840px;width:124px">Case Studies</a>
  <a style="left:984px;width:80px">Pricing</a>
  <a style="left:1086px;width:83px">Contact</a>
</nav>

<section class="abs hero">
  <p class="abs hero-q" style="top:55px">What do <em>users think</em> about your product?</p>
  <p class="abs hero-q" style="top:92px">Are your <em>clients satisfied</em> with your services?</p>
  <p class="abs hero-q" style="top:129px">Does your company create a <em>positive vibe</em> on the Internet?</p>
</section>
<div class="abs cta">VantaLume knows the answer.</div>
<svg class="abs cta-tail" width="22" height="18" viewBox="0 0 22 18"><path d="M0 0H22L4 18Z" fill="#8d6cbd"/></svg>
<div class="abs hero-art" role="img" aria-label="Illustration of purple and green data cylinders over scattered report sheets"></div>

<section class="abs band">
  <div class="abs band-icon" style="left:45px;background:linear-gradient(#f2c04a,#5aa0e0)" role="img" aria-label="Chart report icon"></div>
  <p class="abs band-item" style="left:120px">Get comprehensive charts, graphs and reports. Results with quick overview.</p>
  <div class="abs divider" style="left:385px"></div>
  <div class="abs band-icon" style="left:412px;background:linear-gradient(#9ad14a,#e06ab0)" role="img" aria-label="Speech bubbles icon"></div>
  <p class="abs band-item" style="left:499px;width:250px">It´s also about the details - you get quotations and exact thoughts from your customers.</p>
  <div class="abs divider" style="left:768px"></div>
  <svg class="abs" style="left:785px;top:40px" width="56" height="40" viewBox="0 0 56 40"><path d="M2 12H30V2L54 20L30 38V28H2Z" fill="#8fd43a"/></svg>
  <p class="abs band-item" style="left:861px;width:250px">Take your marketing surveys further - we have the skills, the technique and equipment.</p>
</section>

<h2 class="abs" style="left:87px;top:610px">About VantaLume</h2>
<p class="abs body" style="left:84px;top:661px;width:330px">Duis eu ipsum sed orci tincidunt rutrum. Pellentesque a justo eget odio bibendum venenatis sed at tellus. Nulla non neque sit amet leo placerat.</p>
<div class="abs btn-small">About VantaLume</div>

<h2 class="abs" style="left:452px;top:610px">Our Services</h2>
<ul class="abs services">
  <li style="margin-top:0"><svg width="16" height="14" viewBox="0 0 16 14"><path d="M1 7L6 12L15 1" stroke="#d58ac6" stroke-width="2.5" fill="none"/></svg>Acerat incidunt rutrum pellentesque justo parturient montes</li>
  <li style="margin-top:18px"><svg width="16" height="14" viewBox="0 0 16 14"><path d="M1 7L6 12L15 1" stroke="#d58ac6" stroke-width="2.5" fill="none"/></svg>Eget odio bibendum venenatis</li>
  <li style="margin-top:18px"><svg width="16" height="14" viewBox="0 0 16 14"><path d="M1 7L6 12L15 1" stroke="#d58ac6" stroke-width="2.5" fill="none"/></svg>Suspendisse interdum arcu in nisl condimentum</li>
  <li style="margin-top:18px"><svg width="16" height="14" viewBox="0 0 16 14"><path d="M1 7L6 12L15 1" stroke="#d58ac6" stroke-width="2.5" fill="none"/></svg>Nulla non neque sit phasellus sed mauris a sem mattis</li>
</ul>

<h2 class="abs" style="left:825px;top:610px">Contact Us</h2>
<div class="abs contact">
  <p><strong>VantaLume Ltd.</strong></p>
  <p style="margin-top:15px">42 Harlow Lane<br>QPX RT 4410, London, United Kingdom</p>
  <p style="margin-top:22px"><span style="display:inline-block;width:92px">Tel:</span>0044-555-01924<br><span style="display:inline-block;width:92px">E-mail:</span><a>info@vantalume.example</a></p>
</div>

<section class="abs clients">
  <p class="abs clients-label">Some of our clients...</p>
  <span class="abs client" style="left:271px">Ivemark</span>
  <span class="abs client" style="left:414px">Intara</span>
  <span class="abs client" style="left:555px">Unova</span>
  <span class="abs client" style="left:697px">Nordia</span>
  <span class="abs client hover" style="left:837px">Genova</span>
  <span class="abs client" style="left:979px">Wavero</span>
</section>

<p class="abs footer" style="left:84px">Copyright 2010, VantaLume Ltd.</p>
<p class="abs footer" style="left:325px"><a>Terms of Use</a> &nbsp;/&nbsp; <a>Contact</a></p>
<div class="abs social" style="left:942px">
  <span style="font-size:13px;margin-right:6px">Follow us via</span>
  <span class="sq"></span>Pagenet
  <span class="sq" style="margin-left:4px"></span>Chirpa
  <span class="sq" style="margin-left:4px;background:#e58a2e"></span>Newsflow
</div>

</body>
</html>
```